Design a Flyer/Poster for a Mountain Adventure Event

We need a flyer designed to be printed on 8.5" x 11" paper to advertise an event entitled Cobalt Quest 2014. The copy has already been written. The end result will need to be delivered in a fully editable format (Adobe Illustrator or other Adobe product is preferred). All components of the final deliverable file must be easily editable with appropriate software, as details of this event may change before printing. The final deliverable must also be in a high resolution (min 300dpi) for glossy printing at 8.5" x 11" printed size.

This event is still in concept phase, and the website does not yet exist. Ideas for images are attached below - I do not have rights to use those particular images. In addition to the photo ideas, I have attached versions of the logo for the organization that will benefit from the event (Center for Pellam & Orrin Inquiry). One of those logos will need to be used (probably towards bottom of flyer/poster) with the text: Benefiting the Center for Pellam & Orrin Inquiry

Text for Flyer/Poster:
Cobalt Quest 2014
June 15 - 30

1. Run/Hike in the Mountains between June 15-30, 2014
2. Track it with GPS or Satellite
3. Follow your Competitors online

Compete for:
Most Elevation Gain
Most Miles
Most Summits
Best Photos
Best Family Adventures

Prizes awarded by Age Class, Gender, Individuals & Teams
You could win $1,000!

Where:
Mountains of your Choice

Registration: $99 (Limited to 500 Participants)
Optional: Rent a Trava K7TM with Unlimited Tracking: $99

Benefiting the Center for Pellam & Orrin Inquiry

```html
<!DOCTYPE html>
<html lang="en">
<head>
<meta charset="utf-8">
<title>Cobalt Quest 2014 Flyer</title>
<link href="https://fonts.googleapis.com/css2?family=Open+Sans:wght@400;600;700&display=swap" rel="stylesheet">
<style>
  :root {
    --sky-top: #9cc6e6;
    --sky-mid: #5aa6dc;
    --blue-deep: #2a86cc;
    --blue-bottom: #3d98d8;
    --mountain-green: #6f8f55;
    --panel-grey: rgba(120, 128, 136, 0.62);
    --panel-teal: rgba(110, 190, 205, 0.62);
    --white: #ffffff;
    --prize-green: #2fa84a;
    --url-green: #1f6e3a;
    --banner-blue: #1b33b8;
    --banner-light: #e9f1f7;
    --banner-shade: #9fb6c8;
    --brand-teal: #2a7f9c;
  }
  * { margin: 0; padding: 0; box-sizing: border-box; }
  html, body { width: 928px; height: 1200px; overflow: hidden; }
  body {
    font-family: "Open Sans", Arial, sans-serif;
    color: var(--white);
  }
  .flyer {
    position: relative;
    width: 928px;
    height: 1200px;
    overflow: hidden;
    background: linear-gradient(180deg, var(--sky-mid) 0%, var(--blue-deep) 55%, var(--blue-bottom) 100%);
  }
  .hero-photo {
    position: absolute;
    left: 0; top: 0;
    width: 928px; height: 700px;
    background: linear-gradient(180deg, var(--sky-top) 0%, #b9d4e6 30%, #7f9a8a 48%, var(--mountain-green) 62%, #5d7f5a 80%, rgba(74,150,210,0) 100%);
    -webkit-mask-image: linear-gradient(180deg, #000 75%, transparent 100%);
            mask-image: linear-gradient(180deg, #000 75%, transparent 100%);
  }
  .brand-top {
    position: absolute;
    left: 232px; top: 22px;
    display: flex; align-items: center; gap: 14px;
  }
  .brand-mark {
    width: 130px; height: 100px;
    border-radius: 50%;
    background: var(--brand-teal);
    opacity: 0.85;
  }
  .brand-name {
    font-weight: 600;
    font-size: 25px;
    line-height: 1.05;
    letter-spacing: 3px;
    color: var(--brand-teal);
    text-transform: uppercase;
  }
  .info-panel {
    position: absolute;
    left: 433px; top: 150px;
    width: 483px; height: 541px;
    background: var(--panel-grey);
    border-radius: 8px;
    padding: 16px 20px 0 22px;
  }
  .event-title {
    font-weight: 700;
    font-size: 31px;
    line-height: 1.3;
    text-align: center;
    padding-right: 10px;
  }
  .steps {
    list-style: none;
    margin-top: 10px;
    font-size: 24px;
    line-height: 1.32;
  }
  .steps .wrap { display: block; padding-left: 52px; }
  .compete { margin-top: 10px; font-size: 27px; line-height: 1.53; }
  .prize-box {
    position: absolute;
    left: 21px; top: 510px;
    width: 338px; height: 201px;
    background: var(--panel-teal);
    border-radius: 6px;
    padding: 16px 0 0 14px;
    font-size: 26px;
    line-height: 1.5;
  }
  .prize-box .amount { color: var(--prize-green); }
  .where {
    position: absolute;
    left: 18px; top: 766px;
    font-size: 30px;
    line-height: 1.45;
  }
  .photo {
    position: absolute;
    border: 3px solid var(--white);
    box-shadow: 0 3px 8px rgba(0,0,0,0.35);
  }
  .photo-fjord { left: 450px; top: 704px; width: 198px; height: 108px;
    background: linear-gradient(180deg, #9fb9cf 0%, #5f7a86 45%, #4d5d55 100%); }
  .photo-summit { left: 596px; top: 764px; width: 196px; height: 141px;
    background: linear-gradient(180deg, #7fb2e6 0%, #c9dcec 55%, #6c6860 100%); }
  .photo-trail { left: 776px; top: 843px; width: 141px; height: 190px;
    background: linear-gradient(180deg, #bcd6ea 0%, #7a9a5a 40%, #5f7f3d 100%); }
  .registration {
    position: absolute;
    left: 19px; top: 900px;
    font-size: 22px;
    line-height: 1.72;
  }
  .brand-bottom {
    position: absolute;
    left: 30px; top: 1000px;
    width: 140px;
    text-align: center;
  }
  .brand-bottom .brand-mark { width: 130px; height: 120px; margin: 0 auto 8px; }
  .brand-bottom .brand-initials {
    font-weight: 400;
    font-size: 30px;
    letter-spacing: 8px;
    color: var(--brand-teal);
  }
  .banner {
    position: absolute;
    left: 206px; top: 1054px;
    width: 700px; height: 80px;
  }
  .banner svg { position: absolute; left: 0; top: 0; }
  .banner-text {
    position: absolute;
    left: 60px; top: 24px; width: 620px;
    text-align: center;
    font-size: 20px;
    color: var(--banner-blue);
  }
  .site-url {
    position: absolute;
    left: 206px; top: 1136px; width: 700px;
    text-align: center;
    font-size: 28px;
    color: var(--url-green);
  }
</style>
</head>
<body>
<main class="flyer">
  <div class="hero-photo" role="img" aria-label="Photo of four smiling hikers standing beside a stone cairn on a sunny mountain ridge with valleys behind"></div>

  <header class="brand-top">
    <div class="brand-mark"></div>
    <div class="brand-name">Center for<br>Pellam &amp; Orrin<br>Inquiry</div>
  </header>

  <section class="info-panel">
    <h1 class="event-title">Cobalt Quest 2014<br>June 15 - 30</h1>
    <ol class="steps">
      <li>1. Run/Hike in the Mountains bet-<span class="wrap">ween June 15-30, 2014</span></li>
      <li>2. Track it with GPS or Satellite</li>
      <li>3. Follow your Competitors online</li>
    </ol>
    <div class="compete">
      Compete for:<br>
      Most Elevation Gain<br>
      Most Miles<br>
      Most Summits<br>
      Best Photos<br>
      Best Family Adventures
    </div>
  </section>

  <section class="prize-box">
    Prizes awarded by:<br>
    Age Class, Gender,<br>
    Individuals &amp; Teams<br>
    You could win <span class="amount">$1,000!</span>
  </section>

  <section class="where">Where:<br>Mountains of your Choice</section>

  <div class="photo photo-fjord" role="img" aria-label="Photo of a hiker on a rocky cliff above a fjord"></div>
  <div class="photo photo-summit" role="img" aria-label="Photo of a hiker with outstretched arms on a summit under blue sky"></div>
  <div class="photo photo-trail" role="img" aria-label="Photo of a runner on a grassy mountain trail"></div>

  <section class="registration">
    Registration: $99 (Limited to 500 Participants)<br>
    Optional: Rent a Trava K7TM with Unlimited Tracking: $99
  </section>

  <div class="brand-bottom">
    <div class="brand-mark"></div>
    <div class="brand-initials">CPOI</div>
  </div>

  <div class="banner">
    <svg width="700" height="80" viewBox="0 0 700 80" aria-hidden="true">
      <defs>
        <linearGradient id="bannerFill" x1="0" y1="0" x2="0" y2="1">
          <stop offset="0" stop-color="#ffffff"/>
          <stop offset="0.6" stop-color="#e4eef6"/>
          <stop offset="1" stop-color="#c7d8e6"/>
        </linearGradient>
        <linearGradient id="curlFill" x1="0" y1="0" x2="1" y2="0">
          <stop offset="0" stop-color="#7f99ae"/>
          <stop offset="0.5" stop-color="#dfe9f2"/>
          <stop offset="1" stop-color="#8ea8bc"/>
        </linearGradient>
      </defs>
      <path d="M30 14 Q360 4 698 18 L690 70 Q360 60 30 70 Z" fill="url(#bannerFill)"/>
      <rect x="6" y="6" width="34" height="70" rx="14" fill="url(#curlFill)"/>
      <ellipse cx="23" cy="8" rx="17" ry="5" fill="#b9cbd9"/>
    </svg>
    <div class="banner-text">Benefiting the Center for Pellam &amp; Orrin Inquiry</div>
  </div>

  <footer class="site-url">CobaltQuest2014.com</footer>
</main>
</body>
</html>
```